Web Design Project

We are an IT System Integrator. We provide Norvik 500 ERP System, CRM etc. We also provide hardware, networking servicing. Please look at www.brinquot.com.sg. They provide the same service as us. We like to redesign our web site. I will attached the color that I prefer for reference.

Our website is www.ravdu.com.sg.  It has been created about 14 years ago.  We are trying to revamp it with a new look and information.   The new website must be informative, fast.    I have attached an attachment which show the color that I prefer(brownish golden).   

Our competitor (www.brinquot.com) is carrying the same trade as us.  They have all the informations In their website that we will like to have.  Therefore I recommend you to take a look at my competitor website and have a better   
understanding on the kind of information I would like to have for my new website.

This project is guarantee to the person with the best design.  We can have it guarantee.

Target Market(s)

Corporate and companies

Industry/Entity Type

Hardware

```html
<!DOCTYPE html>
<html lang="en">
<head>
<meta charset="utf-8">
<title>Ravdu Information Systems</title>
<link href="https://fonts.googleapis.com/css2?family=Open+Sans:wght@300;400;600;700&family=Roboto+Condensed:wght@400;700&display=swap" rel="stylesheet">
<style>
:root{
  --gold:#e8a21e;
  --gold-deep:#c9791a;
  --gold-light:#f2c14a;
  --ink:#333;
  --text:#555;
  --nav:#1f1610;
  --topbar:#e9e9e9;
  --footer-mid:#2c2c2c;
  --bottom:#262626;
  --line:#e2e2e2;
}
*{margin:0;padding:0;box-sizing:border-box}
html,body{width:822px;height:1200px;overflow:hidden;background:#fff}
body{font-family:"Open Sans",sans-serif;color:var(--text)}
h1,h2,h3{font-weight:400}
.page{position:relative;width:822px;height:1200px;overflow:hidden;background:#fafafa}
.abs{position:absolute}

.topbar{left:0;top:0;width:822px;height:22px;background:var(--topbar);border-bottom:1px solid #d8d8d8}
.social{display:flex;gap:3px}
.social span{width:11px;height:11px;border-radius:50%;background:#3a3a3a;display:block}
.topbar .social{position:absolute;left:73px;top:5px}
.toplinks{position:absolute;right:70px;top:6px;font-size:7.5px;color:#333;letter-spacing:.1px}

.header{left:0;top:22px;width:822px;height:102px;background:#fff}
.brand{position:absolute;left:74px;top:28px;display:flex;align-items:center;gap:6px}
.brand-dot{width:14px;height:14px;border-radius:50%;background:var(--gold-deep)}
.brand-name{font-weight:700;font-size:30px;color:var(--gold-deep);line-height:1}
.phone-block{position:absolute;left:595px;top:28px;display:flex;align-items:center;gap:8px}
.phone-label{font-size:10px;font-weight:700;color:var(--gold-deep);letter-spacing:.2px}
.phone-number{font-size:18px;color:#333;line-height:1.1}

.hero{left:0;top:124px;width:822px;height:294px;background:radial-gradient(ellipse at 40% 50%,#f2c23b 0%,#e3a224 45%,#c9791a 100%)}
.hero-fade{left:0;top:418px;width:822px;height:64px;background:linear-gradient(#f1f1f1,#fafafa)}
.hero-title{left:72px;top:232px;font-size:39px;font-weight:300;color:#fff;letter-spacing:.5px}
.hero-sub{left:73px;top:284px;width:235px;font-size:16px;line-height:22px;color:#fbe39b}
.hero-art{left:314px;top:198px;width:402px;height:259px;border-radius:8px;background:linear-gradient(100deg,#1f79d4 0%,#2a93e6 30%,#8a8e95 45%,#2a2c30 70%,#4b4e54 100%)}
.arrow{top:255px}

.nav{left:67px;top:108px;width:685px;height:34px;background:var(--nav);display:flex;align-items:center;padding-left:12px}
.nav a{font-size:10.5px;color:var(--gold-light);text-decoration:none;padding:0 17px;position:relative}
.nav a + a::before{content:"";position:absolute;left:0;top:2px;height:10px;border-left:1px solid #6b5230}
.nav a.active{color:#fff}
.nav-underline{left:67px;top:139px;width:65px;height:3px;background:#fff}

.welcome-title{left:69px;top:524px;font-family:"Roboto Condensed",sans-serif;font-size:22px;color:var(--ink)}
.welcome-photo{left:67px;top:563px;width:129px;height:128px;border:1px solid #999;background:linear-gradient(135deg,#cfd6dd,#9aa4ae 60%,#e9ecef)}
.welcome-lead{left:209px;top:561px;width:250px;font-size:12.8px;line-height:17px;color:var(--gold)}
.welcome-body{font-size:10.2px;line-height:15px;color:#555}
.wb1{left:209px;top:659px;width:240px}
.wb2{left:67px;top:703px;width:395px}
.divider-v{left:470px;top:531px;width:1px;height:207px;background:var(--line)}

.side-title{font-family:"Roboto Condensed",sans-serif;font-size:18px;color:var(--ink)}
.testi-title{left:495px;top:529px}
.testi-logo{left:496px;top:563px;width:46px;height:45px;background:#f1d21a}
.quote{font-family:Georgia,serif;font-size:22px;color:#aaa;line-height:1}
.q1{left:550px;top:558px}.q2{left:732px;top:618px}
.testi-text{left:572px;top:566px;width:182px;font-size:10px;line-height:15px;color:#555}
.testi-who{left:540px;top:617px;width:186px;text-align:right;font-size:10px;color:var(--gold)}
.side-rule{left:495px;top:650px;width:257px;height:1px;background:var(--line)}
.news-title{left:495px;top:669px}
.news-badge{left:497px;top:703px;width:27px;height:36px}
.news-text{left:534px;top:706px;width:218px;font-size:10px;line-height:14.5px;font-weight:600;color:#555}

.dark{left:0;top:838px;width:822px;height:320px;background:linear-gradient(#474747,#3a3a3a 60%,#333)}
.partners{left:67px;top:773px;width:685px;height:85px;background:#fff;border:1px solid #ddd;box-shadow:0 10px 18px rgba(0,0,0,.35)}
.partners-tab{position:absolute;left:0;top:0;width:142px;height:83px;background:#f0f0f0}
.partners-label{position:absolute;left:17px;top:30px;font-family:"Roboto Condensed",sans-serif;font-size:20px;color:var(--ink)}
.badge{position:absolute;top:22px;height:40px;background:#8a8a8a;border-radius:4px}
.sep{position:absolute;top:14px;width:1px;height:56px;background:#e2e2e2}

.big-head{left:0;top:896px;width:822px;text-align:center;font-family:"Roboto Condensed",sans-serif;font-weight:700;font-size:37px;color:#e9e9e9;text-shadow:0 2px 3px rgba(0,0,0,.5)}
.cta-phone-icon{left:219px;top:966px}
.cta-phone{left:259px;top:971px;font-family:"Roboto Condensed",sans-serif;font-size:17px;color:var(--gold-light);white-space:nowrap}
.cta-btn{left:378px;top:958px;width:176px;height:43px;border-radius:22px;background:linear-gradient(#f5cf55,#e3a21e 60%,#c98515);box-shadow:0 6px 10px rgba(0,0,0,.45);display:flex;align-items:center;justify-content:center;font-family:"Roboto Condensed",sans-serif;font-size:20px;color:#2a1d0c}

.footer-mid{left:332px;top:1033px;width:152px;height:125px;background:var(--footer-mid)}
.foot-title{font-size:13px;font-weight:700;color:#fff}
.ft1{left:70px;top:1054px}.ft2{left:375px;top:1054px}.ft3{left:506px;top:1054px}
.foot-text{font-size:8.4px;line-height:12px;color:#ddd}
.services-text{left:70px;top:1080px;width:240px}
.details{left:70px;top:1118px;font-size:8.6px;font-weight:700;color:var(--gold-light)}
.product-list{left:375px;top:1079px;list-style:none}
.product-list li{font-size:8.4px;color:#ddd;line-height:15.2px}
.product-list li::before{content:"»";color:var(--gold);margin-right:6px}
.address{left:507px;top:1079px;line-height:15px}
.address .tel{color:var(--gold-light);font-weight:700}
.map{left:628px;top:1057px;width:114px;height:81px;background:linear-gradient(135deg,#c9d8c0,#e3e6d6 50%,#a9c3de);border:2px solid #fff}

.bottom{left:0;top:1158px;width:822px;height:42px;background:var(--bottom)}
.bottom .social{position:absolute;left:77px;top:15px;gap:5px}
.bottom .social span{width:16px;height:16px;background:#555}
.copyright{position:absolute;right:79px;top:16px;font-size:8.4px;color:#888}
</style>
</head>
<body>
<div class="page">

  <div class="abs topbar">
    <div class="social"><span></span><span></span><span></span><span></span><span></span></div>
    <div class="toplinks">ENQUIRY | LOG INCIDENT | CAREERS | CLIENT SUPPORT | INFOBIN | SITEMAP</div>
  </div>

  <header class="abs header">
    <div class="brand"><span class="brand-dot"></span><span class="brand-name">Ravdu</span></div>
    <div class="phone-block">
      <svg width="22" height="34" viewBox="0 0 22 34" aria-hidden="true"><rect x="1.5" y="1.5" width="19" height="31" rx="3" fill="none" stroke="#444" stroke-width="2"/><line x1="1.5" y1="6" x2="20.5" y2="6" stroke="#444" stroke-width="1.5"/><line x1="1.5" y1="27" x2="20.5" y2="27" stroke="#444" stroke-width="1.5"/></svg>
      <div><div class="phone-label">SINGAPORE</div><div class="phone-number">(065) 6210-4470</div></div>
    </div>
  </header>

  <section class="abs hero" aria-label="Featured service"></section>
  <div class="abs hero-fade"></div>
  <div class="abs hero-art" role="img" aria-label="Blue globe beside a rack of servers"></div>
  <div class="abs hero-title">SERVERS</div>
  <div class="abs hero-sub">Server is a computer on a network that is dedicated to a particular purpose...</div>
  <svg class="abs arrow" style="left:13px" width="22" height="62" viewBox="0 0 22 62" aria-hidden="true"><polyline points="20,2 2,31 20,60" fill="none" stroke="#fff" stroke-width="1.5"/></svg>
  <svg class="abs arrow" style="left:788px" width="22" height="62" viewBox="0 0 22 62" aria-hidden="true"><polyline points="2,2 20,31 2,60" fill="none" stroke="#fff" stroke-width="1.5"/></svg>

  <nav class="abs nav">
    <a class="active">HOME</a><a>COMPANY</a><a>SERVICES</a><a>PRODUCTS</a><a>PARTNERS</a><a>NORVIK</a><a>CLIENTELE</a><a>CONTACT US</a>
  </nav>
  <div class="abs nav-underline"></div>

  <h1 class="abs welcome-title">Welcome To Ravdu Information Systems</h1>
  <div class="abs welcome-photo" role="img" aria-label="Two colleagues working at a laptop in an office"></div>
  <p class="abs welcome-lead">Based in Singapore with 11 years of establishment, 250 local &amp; regional customers, 300 project implementations, 1000 satisfied users and we are still growing.</p>
  <p class="abs welcome-body wb1">Ravdu Information Systems Pte Ltd (RIS) is professionally managed by a core group of</p>
  <p class="abs welcome-body wb2">visionaries and technologists with decades of industry experience between them and backed by a team of trained professionals at all levels of operations. Perfection is a way of life at RIS.</p>
  <div class="abs divider-v"></div>

  <h2 class="abs side-title testi-title">Testimonials</h2>
  <div class="abs testi-logo" role="img" aria-label="Client badge"></div>
  <div class="abs quote q1">&ldquo;</div>
  <p class="abs testi-text">The greatest benefit was that I see no more sulky face or user they are happy doing away their invoices...</p>
  <div class="abs testi-who">General Manager at Lunmar Foods</div>
  <div class="abs quote q2">&rdquo;</div>
  <div class="abs side-rule"></div>
  <h2 class="abs side-title news-title">News</h2>
  <svg class="abs news-badge" viewBox="0 0 27 36" aria-hidden="true"><path d="M0 4h27v26l-6 6H0z" fill="#d89a28"/><rect x="5" y="0" width="3" height="7" fill="#9a6a14"/><rect x="19" y="0" width="3" height="7" fill="#9a6a14"/><text x="13" y="27" text-anchor="middle" font-family="Open Sans,sans-serif" font-weight="700" font-size="12" fill="#fff">01</text></svg>
  <p class="abs news-text">Expanding the Boundaries with Korvo-ERP Integration Workshop</p>

  <div class="abs dark"></div>
  <div class="abs partners">
    <div class="partners-tab"></div>
    <svg style="position:absolute;left:142px;top:0" width="22" height="83" aria-hidden="true"><polygon points="0,0 22,41.5 0,83" fill="#f0f0f0"/></svg>
    <div class="partners-label">Our Partners</div>
    <div class="badge" style="left:188px;width:54px;height:54px;top:15px;border-radius:50%"></div>
    <div class="sep" style="left:258px"></div>
    <div class="badge" style="left:279px;width:78px"></div>
    <div class="sep" style="left:378px"></div>
    <div class="badge" style="left:398px;width:80px;top:30px;height:22px"></div>
    <div class="sep" style="left:481px"></div>
    <div class="badge" style="left:503px;width:50px;height:50px;top:17px"></div>
    <div class="sep" style="left:575px"></div>
    <div class="badge" style="left:592px;width:80px;top:29px;height:26px"></div>
  </div>

  <h2 class="abs big-head">250 LOCAL &amp; REGIONAL CUSTOMERS</h2>
  <svg class="abs cta-phone-icon" width="32" height="30" viewBox="0 0 32 30" aria-hidden="true"><path d="M2 10c0-5 28-5 28 0v3h-8v-3c-4-1-8-1-12 0v3H2z" fill="#e8a21e"/><path d="M8 14h16l5 14H3z" fill="#e8a21e"/><circle cx="16" cy="21" r="4" fill="#3c3c3c"/></svg>
  <div class="abs cta-phone">(065) 6210-4470</div>
  <div class="abs cta-btn">CONTACT US</div>

  <div class="abs footer-mid"></div>
  <h3 class="abs foot-title ft1">Services</h3>
  <p class="abs foot-text services-text">The principal business activities of RIS are implementing of Norvik Accounting software, networking, hardware maintenance and consulting assistance.</p>
  <div class="abs details">Details »</div>
  <h3 class="abs foot-title ft2">Products</h3>
  <ul class="abs product-list"><li>Recent Work</li><li>Before / After</li><li>Commerical</li><li>About Us</li></ul>
  <h3 class="abs foot-title ft3">Company</h3>
  <p class="abs foot-text address">18 Kelsor Lane<br># 03-21/22 Harbor Point<br>Singapore - 518842<br><span class="tel">(065) 6210-4470</span></p>
  <div class="abs map" role="img" aria-label="Location map of the office"></div>

  <footer class="abs bottom">
    <div class="social"><span></span><span></span><span></span><span></span><span></span></div>
    <div class="copyright">© Copyrights 2013. Ravdu Information Systems. All Rights Reserved.</div>
  </footer>
</div>
</body>
</html>
```